Business Card Design Project for International Business Consultanting Firm

Korvane International was established in 1998 and most recently updated our logo.
We provide advice and consultation regarding international business deals; we are also business brokers; and consultants to entreprenueurs. Excellence across borders is our slogan.

Our Previous business card we had Korvane International and under that; Business Brokers, Int'l Consultants, Finance, Travel and Tourism. I think we branded ourselves too broad so i will keep within the scope of Business and Finance Brokers Domestic and International.

We are looking for a design that conveys modern elegance with simplicity, and class as well as communicate safety and stability.

Target Market(s)

International and domestic business people, entrepreneurs and professionals

Industry/Entity Type

Safety

Requirements
Must have
• Both sides of the business card must be designed.

Must include our logo which is attached.

I am open to modern sophisticated elegance.

Be extremely creative.

Include an area for name, title, business address, telephone, email address and website address

The look must be polished and clever
Nice to have
• maybe two-tone business card; one side vs the other

```html
<!DOCTYPE html>
<html lang="en">
<head>
<meta charset="utf-8">
<title>Korvane International — Business Card</title>
<link rel="stylesheet" href="https://fonts.googleapis.com/css2?family=EB+Garamond:wght@400&family=Questrial&family=PT+Sans&display=swap">
<style>
  :root {
    --page-bg: #ece9e4;
    --card-white: #ffffff;
    --brand-blue: #1b6499;
    --brand-blue-deep: #16649c;
    --swoosh-grey: #9a9c9f;
    --text-grey: #444444;
    --label-ink: #111111;
    --mark-fill: #e4e9f0;
    --mark-faint: #eef1f6;
    --card-shadow: 0 4px 14px rgba(0,0,0,.25);
  }
  * { box-sizing: border-box; margin: 0; padding: 0; }
  html, body { width: 1200px; height: 788px; overflow: hidden; }
  body { background: var(--page-bg); position: relative; font-family: "Questrial", sans-serif; }

  .side-label {
    position: absolute; width: 300px; text-align: center;
    font-family: "PT Sans", sans-serif; font-size: 21px; color: var(--label-ink);
  }

  .card {
    position: absolute; width: 525px; height: 299px; border-radius: 22px;
    background: var(--card-white); box-shadow: var(--card-shadow); overflow: hidden;
  }
  .card--blue { background: var(--brand-blue-deep); }

  .brand-mark { position: absolute; border-radius: 50%; background: var(--mark-fill); }
  .card--blue .brand-mark { background: var(--card-white); }

  .brand-name {
    position: absolute; white-space: nowrap;
    font-family: "EB Garamond", serif; font-weight: 400; color: var(--brand-blue); line-height: 1;
  }
  .card--blue .brand-name { color: var(--card-white); }

  .web-line {
    position: absolute; left: 0; width: 100%; text-align: center;
    font-size: 13px; letter-spacing: 3px; color: var(--text-grey);
  }
  .card--blue .web-line { color: var(--card-white); }

  /* Front */
  .front .divider { position: absolute; left: 340px; top: 53px; width: 1px; height: 128px; background: #888; }
  .contact { position: absolute; left: 353px; top: 56px; }
  .contact__name { font-family: "EB Garamond", serif; font-size: 21px; color: var(--brand-blue); line-height: 1.1; }
  .contact__title { font-family: "EB Garamond", serif; font-size: 16px; color: var(--text-grey); margin-bottom: 8px; }
  .contact__line { font-size: 13px; color: var(--text-grey); line-height: 18px; }
  .contact__line b { font-style: italic; font-weight: 700; color: #222; }
  .front .wave { position: absolute; left: 0; top: 0; }
  .address { position: absolute; left: 45px; top: 252px; font-size: 13px; color: var(--card-white); line-height: 18px; }
</style>
</head>
<body>

  <div class="side-label" style="left:170px; top:33px;">Front</div>
  <div class="side-label" style="left:746px; top:33px;">Back - 1</div>
  <div class="side-label" style="left:174px; top:404px;">Back - 2</div>
  <div class="side-label" style="left:746px; top:404px;">Back - 3</div>

  <!-- Front -->
  <section class="card front" style="left:57px; top:75px;">
    <svg class="wave" width="525" height="299" viewBox="0 0 525 299">
      <path d="M112,219 C200,221 270,256 340,256 C420,256 480,232 525,218 L525,226 C480,244 420,264 340,264 C270,264 200,224 112,219 Z" fill="var(--swoosh-grey)"/>
      <path d="M0,243 C40,228 80,220 120,221 C200,222 270,270 340,272 C420,274 480,260 525,246 L525,299 L0,299 Z" fill="var(--brand-blue)"/>
    </svg>
    <div class="brand-mark" style="left:125px; top:55px; width:90px; height:90px;"></div>
    <div class="brand-name" style="left:18px; top:150px; font-size:35px;">Korvane International</div>
    <div class="divider"></div>
    <div class="contact">
      <div class="contact__name">Your Name</div>
      <div class="contact__title">Designation</div>
      <div class="contact__line"><b>c</b> : +12 345 67 8910</div>
      <div class="contact__line"><b>p</b> : +12 345 67 8910</div>
      <div class="contact__line"><b>e</b> : name@website.com</div>
      <div class="contact__line"><b>w</b> : www.website.com</div>
    </div>
    <div class="address">123 Abc Street<br>0000 city, country</div>
  </section>

  <!-- Back 1 -->
  <section class="card" style="left:622px; top:75px;">
    <div class="brand-mark" style="left:198px; top:53px; width:124px; height:124px;"></div>
    <div class="brand-name" style="left:0; width:100%; text-align:center; top:182px; font-size:50px;">Korvane International</div>
    <div class="web-line" style="top:269px;">www.website.com</div>
  </section>

  <!-- Back 2 -->
  <section class="card" style="left:54px; top:446px;">
    <div class="brand-mark" style="left:131px; top:9px; width:255px; height:255px; background:var(--mark-faint);"></div>
    <div class="brand-name" style="left:0; width:100%; text-align:center; top:117px; font-size:54px;">Korvane International</div>
    <div class="web-line" style="top:257px;">www.website.com</div>
  </section>

  <!-- Back 3 -->
  <section class="card card--blue" style="left:622px; top:446px;">
    <div class="brand-mark" style="left:195px; top:31px; width:136px; height:136px;"></div>
    <div class="brand-name" style="left:0; width:100%; text-align:center; top:173px; font-size:53px;">Korvane International</div>
    <div class="web-line" style="top:267px;">www.website.com</div>
  </section>

</body>
</html>
```